Corvella Website Homepage

Committed to delivering quality content, quillpagewords.com is a content providing company. Equipped with resourceful writers with industry experience, we promise to empower our clients with content that is tailor-made to address specific requirements of their target Audience.

We need a website home page and one internal page designed. It is very important that the page be laid out with SEO in mind. We like the idea of using five images as navigation to our services. The five major services we offer are:
• Web Content writing (articles, features, website copy etc)
• Business Content writing (Press release, mailers & flyers, brochure/catalog)
• Personal Content writing (blog, speech writing)
• Hire a writer/editor
• Proof reading and editing services
The sample template (http://pv7.layoutdemo-hub.net/dx_48270/index.html) included has five images in the first fold. Designer can choose the right image for each service and lay over the service name on the image. Please do not use flash ( We will use javascripts). We need to have a detailed right side nav as in the template for SEO reasons. There will be some marketing ad- copy below the main images. Followed by a 200 character SEO optimized text defining our services in further detail. Apart from these a designer is free to use his creativity. The name of the site will be http://www.quillpagewords.com/. This name will need a logo too. Please include it as part of design. Corvellacorp is the owner of quillpagewords.com. We already have a logo for Corvella that is attached here as a separate file.

We have some taglines that need to be incorporated in the home page and other pages.
Please provide link button for Home, About us, Services, Samples, Pricing, Clients, Career, Contact us.

Links can be given on TOP, Sideways and Bottom and in the drop down menu of services etc.

Reason: Hi

We have made our project guaranteed and extended deadline by 5 days so you get more time to complete our project.

Thanks and Regards,

Ravindra Kulkarni
Corvellacorp

Target Market(s)

Product Marketing Companies - Mostly in US.
Media companies which publish articles on various subjects. Travel and Lifestyle related sites, Educational Websites, Government Websites, Health related websites,

Industry/Entity Type

Marketing

Requirements
Must have
• Color of Homepage should blend with sober mood of the content. Writing Services should get highlighted in such a way that any person serious about the business visiting the site get attracted to read on the details of our content services. Most space should be used for details of writing services and links for our various pages and services. Webpage should be downloaded in lowest possible time.
Nice to have
• We have some idea about the website layouts;-http://www.skinbazaarly.net/site-layouts/48270.html - layout of information http://www.skinbazaarly.net/site-layouts/47359.html - for kind of marketing http://pv7.layoutdemo-hub.net/dx_48615/index.html - for colors
we attach a word file representing our idea in some way but not limited to it.
Should not have
• Gaudy (aggressive dark) colors. It should not be cluttered. No flash.

```html
<!DOCTYPE html>
<html lang="en">
<head>
<meta charset="utf-8">
<title>quillpagewords.com — Content Writing Services</title>
<link rel="stylesheet" href="https://fonts.googleapis.com/css2?family=Arimo:wght@400;700&display=swap">
<style>
:root{
  --red:#c8171e;
  --red-dark:#a50f15;
  --text:#8a8a8a;
  --ink:#333;
  --page:#f7f7f7;
  --nav-top:#f4f4f4;
  --nav-bottom:#dcdcdc;
  --maroon:#a3233a;
  --green:#3f8f36;
  --orange:#c25f1b;
  --blue:#2b6189;
  --slate:#707070;
  --footer:#222;
  --footer-deep:#2c2c2c;
}
*{box-sizing:border-box;margin:0;padding:0}
html,body{width:1100px;height:1200px;overflow:hidden}
body{font-family:"Arimo",Arial,sans-serif;background:var(--page);position:relative;color:var(--ink)}
.top-rule{position:absolute;left:0;top:0;width:1100px;height:5px;background:var(--red)}
.site-header{position:absolute;left:0;top:5px;width:1100px;height:118px;background:linear-gradient(#fff,#efefef)}
.brand{position:absolute;left:76px;top:40px;display:flex;align-items:center;gap:14px}
.brand-mark{width:26px;height:26px;background:var(--red)}
.brand-name{font-size:35px;color:var(--red);font-weight:400;letter-spacing:-.3px}
.inquiry{position:absolute;left:778px;top:44px;display:flex;gap:18px}
.inquiry-icon{width:44px;height:44px;background:var(--red);border-radius:4px;display:flex;align-items:center;justify-content:center}
.inquiry-label{font-size:14px;font-weight:700;color:#333;letter-spacing:.3px;margin-top:4px}
.inquiry-number{font-size:27px;font-weight:700;color:var(--red);margin-top:3px}
.main-nav{position:absolute;left:0;top:123px;width:1100px;height:43px;border-top:3px solid var(--red);background:linear-gradient(var(--nav-top),var(--nav-bottom))}
.main-nav ul{list-style:none;position:absolute;left:51px;top:0;height:40px;display:flex}
.main-nav li{height:40px;display:flex;align-items:center;justify-content:center;font-size:17px;color:#333;border-right:1px solid #c4c4c4;box-shadow:1px 0 0 #fff}
.main-nav li.is-active{background:var(--red);color:#fff;border-right:none}
.hero-strip{position:absolute;left:51px;top:168px;width:1001px;height:331px;display:flex;gap:2px}
.hero-panel{flex:1;height:100%}
.p1{background:linear-gradient(135deg,#f2f2f2,#9a9a9a 60%,#e4e4e4)}
.p2{background:linear-gradient(160deg,#efefef,#7d7d7d 55%,#f5f5f5)}
.p3{background:linear-gradient(180deg,#3c4a5a,#6f5a45 45%,#d9b45a 85%,#f0e7d5)}
.p4{background:linear-gradient(160deg,#b7b7b7,#5a5a5a 55%,#d0d0d0)}
.p5{background:linear-gradient(140deg,#d6d6d6,#f2f2f2 50%,#8a8a8a)}
.intro-copy{position:absolute;left:65px;top:534px;width:524px;font-size:12.2px;line-height:18.4px;color:var(--text)}
.portrait{position:absolute;left:604px;top:513px;width:182px;height:223px;border:3px solid #c9cfd4;background:linear-gradient(#eef0f2,#b9a695 45%,#2c3446)}
.useful-links{position:absolute;left:808px;top:511px;width:243px;height:225px;background:linear-gradient(#ececec,#e2e2e2);border-radius:0 0 6px 6px;box-shadow:0 2px 3px rgba(0,0,0,.12)}
.useful-links h2{font-size:18px;font-weight:400;color:var(--red);padding:6px 0 6px 18px;border-bottom:1px solid #d0d0d0;box-shadow:0 1px 0 #fafafa}
.useful-links ul{list-style:none;padding:8px 0 0 18px}
.useful-links li{font-size:12.4px;color:var(--text);height:24px;display:flex;align-items:center;gap:14px}
.useful-links li::before{content:"";border-left:5px solid var(--red);border-top:3.5px solid transparent;border-bottom:3.5px solid transparent}
.services{position:absolute;left:51px;top:756px;width:1001px;height:303px;display:flex}
.service{flex:1;border-top:6px solid;position:relative;color:#fff;padding:0 10px}
.service h3{font-size:15px;font-weight:700;text-transform:uppercase;line-height:18px;height:58px;padding-top:22px;letter-spacing:.2px}
.service h3.small{font-size:13px}
.service hr{border:none;border-top:1px dashed rgba(255,255,255,.75);margin:5px -10px 0}
.service p{font-size:12.4px;line-height:17.9px;text-align:justify;padding:10px 2px 0 6px;color:#f4f4f4}
.read-more{position:absolute;left:10px;bottom:18px;height:26px;width:114px;border-radius:5px;display:flex;align-items:center;font-size:12.5px;font-weight:700;color:#fff;box-shadow:0 1px 2px rgba(0,0,0,.35)}
.read-more span{flex:1;text-align:center}
.read-more i{width:24px;height:100%;border-left:1px solid rgba(255,255,255,.4);display:flex;align-items:center;justify-content:center}
.read-more i::after{content:"";border-left:5px solid #fff;border-top:4px solid transparent;border-bottom:4px solid transparent}
.s-web{background:linear-gradient(#b62b45,#8e1d31);border-color:#9e2238}.s-web .read-more{background:linear-gradient(#d94a5e,#b3253a)}
.s-biz{background:linear-gradient(#4aa03f,#35792d);border-color:#3a8a31}.s-biz .read-more{background:linear-gradient(#6cc25e,#3f963a)}
.s-personal{background:linear-gradient(#d06a22,#a94f14);border-color:#b85816}.s-personal .read-more{background:linear-gradient(#ef8a37,#cc6419)}
.s-hire{background:linear-gradient(#316f9c,#214f74);border-color:#265b84}.s-hire .read-more{background:linear-gradient(#4e8fc0,#2d6894)}
.s-proof{background:linear-gradient(#7e7e7e,#5a5a5a);border-color:#666}.s-proof .read-more{background:linear-gradient(#9a9a9a,#6d6d6d)}
.site-footer{position:absolute;left:0;top:1097px;width:1100px;height:103px;background:var(--footer-deep)}
.footer-nav{height:40px;background:var(--footer);border-bottom:1px solid #555;display:flex;justify-content:center}
.footer-nav ul{list-style:none;display:flex;align-items:center;font-size:12.4px;color:#e6e6e6;margin-left:-30px}
.footer-nav li{padding:0 42px;position:relative}
.footer-nav li+li::before{content:"|";position:absolute;left:-3px;color:#ccc}
.footer-nav li.is-active::after{content:"";position:absolute;left:50%;bottom:-15px;margin-left:-5px;border-bottom:5px solid #fff;border-left:5px solid transparent;border-right:5px solid transparent}
.copyright{position:absolute;left:0;top:62px;width:1100px;text-align:center;font-size:12.2px;color:#e0e0e0;padding-right:40px}
.social{position:absolute;left:913px;top:61px;display:flex;gap:6px}
.social span{width:20px;height:20px;background:#8a8a8a;border-radius:3px}
</style>
</head>
<body>
<div class="top-rule"></div>
<header class="site-header">
  <div class="brand"><span class="brand-mark"></span><span class="brand-name">quillpagewords.com</span></div>
  <div class="inquiry">
    <div class="inquiry-icon">
      <svg width="24" height="24" viewBox="0 0 24 24"><path d="M6.6 10.8c1.4 2.8 3.8 5.1 6.6 6.6l2.2-2.2c.3-.3.7-.4 1-.2 1.1.4 2.3.6 3.6.6.6 0 1 .4 1 1V20c0 .6-.4 1-1 1C10.6 21 3 13.4 3 4c0-.6.4-1 1-1h3.5c.6 0 1 .4 1 1 0 1.3.2 2.5.6 3.6.1.3 0 .7-.2 1z" fill="#fff"/></svg>
    </div>
    <div>
      <div class="inquiry-label">CALL FOR INQUIRIES!</div>
      <div class="inquiry-number">123 456 7890</div>
    </div>
  </div>
</header>
<nav class="main-nav">
  <ul>
    <li class="is-active" style="width:111px">HOME</li>
    <li style="width:124px">ABOUT US</li>
    <li style="width:124px">SERVICES</li>
    <li style="width:129px">SAMPLES</li>
    <li style="width:118px">PRICING</li>
    <li style="width:113px">CLIENTS</li>
    <li style="width:121px">CAREER</li>
    <li style="width:161px;border-right:none;box-shadow:none">CONTACT US</li>
  </ul>
</nav>
<section class="hero-strip">
  <div class="hero-panel p1" role="img" aria-label="Photo: hands typing on a keyboard beside paperwork"></div>
  <div class="hero-panel p2" role="img" aria-label="Photo: businesswoman writing at a desk"></div>
  <div class="hero-panel p3" role="img" aria-label="Photo: student writing in front of library shelves"></div>
  <div class="hero-panel p4" role="img" aria-label="Photo: businessman working at a desk"></div>
  <div class="hero-panel p5" role="img" aria-label="Photo: computer mouse, pen and glasses on a desk"></div>
</section>
<p class="intro-copy">Lorem ipsum dolor sit amet, consectetuer adipiscing elit. Aenean commodo ligula eget dolor. Aenean massa. Cum sociis natoque penatibus et magnis dis parturient montes, ridiculus mus. Donec quam felis, ultricies nec, pellentesque eu, pretium quis, sem. Nulla conquat massa quis enim. Donec pede justo, fringilla vel, aliquet nec, vulputate eget, arcu. In enim justo, rhonc ut, imperdiet a, venenatis vitae, justo. Nullam dictum felis eu pede mollis pr Integer tincidunlit. Cras dapibus.Lorem ipsum dolor sit amet, consectetuer adipiscing elit. Aenean commodo ligula eget dolor. Aenean massa. Cum sociis natoque penatibus et magni parturient montescetur ridiculus mus. Donec quam felis, ultricies nec, pellentesque eu, pretium quis,</p>
<div class="portrait" role="img" aria-label="Photo: smiling professional in a suit"></div>
<aside class="useful-links">
  <h2>USEFUL LINKS</h2>
  <ul>
    <li>Lorem ipsum dolor sit amet,</li>
    <li>Lorem ipsum dolor sit amet,</li>
    <li>Lorem ipsum dolor sit amet,</li>
    <li>Lorem ipsum dolor sit amet,</li>
    <li>Lorem ipsum dolor sit amet,</li>
    <li>Lorem ipsum dolor sit amet,</li>
    <li>Lorem ipsum dolor sit amet,</li>
  </ul>
</aside>
<section class="services">
  <article class="service s-web"><h3>Web Content<br>Writing</h3><hr><p>Lorem ipsum dolor sit amet, consectetuer adipiscing elit. Aenean commodo ligula eget dolor. Aenean massa. Cum sociis natoque penatibus-Lorem ipsum dolor sit amet, consectetuer d bbdiscvhsi-uvdsfvsvrpenatibus</p><a class="read-more"><span>READ MORE</span><i></i></a></article>
  <article class="service s-biz"><h3>Business Content<br>Writing</h3><hr><p>Lorem ipsum dolor sit amet, consectetuer adipiscing elit. Aenean commodo ligula eget dolor. Aenean massa. Cum sociis natoque penatibus-Lorem ipsum dolor sit amet, consectetuer d bbdiscvhsi-uvdsfvsvrpenatibus</p><a class="read-more"><span>READ MORE</span><i></i></a></article>
  <article class="service s-personal"><h3 class="small">Personal Content<br>Writing</h3><hr><p>Lorem ipsum dolor sit amet, consectetuer adipiscing elit. Aenean commodo ligula eget dolor. Aenean massa. Cum sociis natoque penatibus-Lorem ipsum dolor sit amet, consectetuer d bbdiscvhsi-uvdsfvsvrpenatibus</p><a class="read-more"><span>READ MORE</span><i></i></a></article>
  <article class="service s-hire"><h3>Hire a Writer/Editor</h3><hr><p>Lorem ipsum dolor sit amet, consectetuer adipiscing elit. Aenean commodo ligula eget dolor. Aenean massa. Cum sociis natoque penatibus-Lorem ipsum dolor sit amet, consectetuer d bbdiscvhsi-uvdsfvsvrpenatibus</p><a class="read-more"><span>READ MORE</span><i></i></a></article>
  <article class="service s-proof"><h3>Proof Reading and<br>Editing Services</h3><hr><p>Lorem ipsum dolor sit amet, consectetuer adipiscing elit. Aenean commodo ligula eget dolor. Aenean massa. Cum sociis natoque penatibus-Lorem ipsum dolor sit amet, consectetuer d bbdiscvhsi-uvdsfvsvrpenatibus</p><a class="read-more"><span>READ MORE</span><i></i></a></article>
</section>
<footer class="site-footer">
  <nav class="footer-nav">
    <ul>
      <li class="is-active">Home</li><li>About us</li><li>Services</li><li>Samples</li><li>Pricing</li><li>Clients</li><li>Career</li><li>Contact us</li>
    </ul>
  </nav>
  <p class="copyright">Copyright @ 2011 quillpagewords.com -&nbsp; All Right Reserved</p>
  <div class="social"><span></span><span></span><span></span><span></span></div>
</footer>
</body>
</html>
```